Introduction flyer

Bright Orchard Nutrition & Wellness Consulting, is a new holistic nutritional therapy specialising in womens health. I want a flyer that appeals to women between 15 to 60. It must speak "health, food & balance". I have attached the basic info I need included in the text. I like Greens & Blues, soft text. My flyer will be distributed to cafes, shops, fitness centres, hung up in grocery stores & health centres etc. The QEVR & WRUK logos need to appear on the flyer to show I am fully registered. My own logo & company name is attached.

Target Market(s)

Women from 10 to 60 years old.

Industry/Entity Type

Nutritionist

Colors
32a6d7
abd037
33b8a4
fbf289
ffcf3e
b768aa
d5d5d5
dcdcdc
e8e8e8

Requirements
Must have
• An image of healthy food & ladies. A group of women eating soup, stews or curry type dishes, with plenty of colour - no bread or white wine, and not just fruit please. Food that looks enjoyable to the average person.
• Nutrition is main part of my job, so please keep that in mind & emphasise food & natural well being.
Should not have
• People exercising, men, white wine, bread, cakes, sweets etc..

```html
<!DOCTYPE html>
<html lang="en">
<head>
<meta charset="utf-8">
<title>Bright Orchard Nutrition &amp; Wellness Consulting – Flyer</title>
<link rel="stylesheet" href="https://fonts.googleapis.com/css2?family=Montserrat:wght@600;700;800&family=Open+Sans:wght@400;600;700&display=swap">
<style>
:root{
  --teal:#33b8a4;
  --teal-dark:#1f9886;
  --green:#abd037;
  --green-dark:#8cb12a;
  --blue:#32a6d7;
  --purple:#b768aa;
  --ink:#4a5a5c;
  --muted:#8a9698;
  --paper:#ffffff;
  --page:#e8e8e8;
}
*{box-sizing:border-box;margin:0;padding:0}
html,body{width:863px;height:1200px;overflow:hidden;background:var(--page)}
.flyer{position:relative;width:863px;height:1200px;background:var(--paper);font-family:"Open Sans",sans-serif;color:var(--ink)}
.hero-photo{position:absolute;left:0;top:0;width:863px;height:470px;
  background:radial-gradient(ellipse at 35% 40%,#f3dcc8 0%,#d7b79a 30%,#9fb0a0 65%,#6e8c86 100%)}
.home-visits{position:absolute;left:585px;top:175px;width:250px;height:250px;border-radius:50%;
  background:var(--green);color:#fff;display:flex;align-items:center;justify-content:center;text-align:center;
  padding:40px;font-family:"Open Sans",sans-serif;font-weight:600;font-size:19px;line-height:1.3;
  border:6px solid rgba(255,255,255,.55)}
.question-band{position:absolute;left:0;top:470px;width:863px;height:112px;background:var(--teal);
  display:flex;align-items:center;justify-content:center;text-align:center;padding:0 50px;
  color:#fff;font-family:"Montserrat",sans-serif;font-weight:700;font-size:23px;line-height:1.3}
.brand{position:absolute;left:34px;top:608px;display:flex;align-items:center;gap:14px;width:340px}
.brand-dot{width:44px;height:44px;border-radius:50%;background:var(--teal);flex:none}
.brand-name{font-family:"Montserrat",sans-serif;font-weight:700;font-size:19px;line-height:1.2;color:var(--teal-dark)}
.intro{position:absolute;left:34px;top:700px;width:248px;color:var(--teal-dark);font-size:13px;line-height:1.5}
.intro h2{font-family:"Montserrat",sans-serif;font-weight:700;font-size:13.5px;line-height:1.35;margin-bottom:12px;text-transform:uppercase}
.intro p{margin-bottom:12px}
.food-photo{position:absolute;left:296px;top:770px;width:136px;height:136px;border-radius:50%;
  background:radial-gradient(circle at 40% 40%,#e6c24a 0%,#b9c94d 35%,#6f9b3e 70%,#8a5a3a 100%);
  border:5px solid #fff;box-shadow:0 0 0 2px var(--green)}
.services{position:absolute;left:450px;top:608px;width:385px}
.services h3{font-family:"Open Sans",sans-serif;font-weight:700;font-size:14.5px;line-height:1.4;color:var(--blue);margin-bottom:14px}
.service-list{list-style:none}
.service-list li{display:flex;gap:10px;align-items:flex-start;font-size:12.5px;line-height:1.35;margin-bottom:9px;color:var(--ink)}
.service-list svg{flex:none;margin-top:1px}
.contact-box{position:absolute;left:440px;top:1030px;width:395px;height:140px;border-radius:18px;background:var(--green);
  color:#fff;text-align:center;padding:14px 18px}
.contact-box .cta{font-family:"Open Sans",sans-serif;font-weight:700;font-size:14px;line-height:1.45}
.contact-box .fine{font-size:8.5px;line-height:1.35;margin-top:8px;opacity:.95}
</style>
</head>
<body>
<main class="flyer">
  <div class="hero-photo" role="img" aria-label="Photo of a smiling woman in a hat enjoying a colourful healthy meal at a table"></div>
  <div class="home-visits">Home visits available, at no extra cost within local area. I can visit your place of work or home.</div>

  <section class="question-band">DO YOU EXPERIENCE LOW ENERGY, LOW LIBIDO, MENSTRUAL CYCLE COMPLICATIONS, OR ARE YOU PLANNINGA BABY?</section>

  <div class="brand">
    <span class="brand-dot"></span>
    <span class="brand-name">Bright Orchard Nutrition &amp; Wellness Consulting</span>
  </div>

  <section class="intro">
    <h2>Small changes to your diet may lead to big changes in your health.</h2>
    <p>Eat well, live well.<br>Discover exactly what YOU need to change and how to make these changes long lasting.</p>
    <p>There is no 1 rule fits all. My nutritional advice aims to dig up the root cause to my client's health concerns. My lifestyle plans are completely personalised to an individual's needs and circumstances.<br>I consider the whole person not just symptoms or disease.</p>
  </section>

  <div class="food-photo" role="img" aria-label="Round photo of a colourful bowl of vegetable stew"></div>

  <section class="services">
    <h3>Qualified, Registered and fully insured Nutritional Therapist &amp; Wellness Consultant, specialising in:</h3>
    <ul class="service-list">
      <li><svg width="14" height="14" viewBox="0 0 14 14"><circle cx="7" cy="7" r="6.5" fill="none" stroke="#abd037"/><path d="M4 7.2l2 2 4-4.4" fill="none" stroke="#abd037" stroke-width="1.6"/></svg>Fertility, IVF, pre-conception, pregnancy &amp; post-natal care</li>
      <li><svg width="14" height="14" viewBox="0 0 14 14"><circle cx="7" cy="7" r="6.5" fill="none" stroke="#abd037"/><path d="M4 7.2l2 2 4-4.4" fill="none" stroke="#abd037" stroke-width="1.6"/></svg>Menstrual cycle challenges (PCOS, Endometriosis, PMS, heavy/irregular periods etc)</li>
      <li><svg width="14" height="14" viewBox="0 0 14 14"><circle cx="7" cy="7" r="6.5" fill="none" stroke="#abd037"/><path d="M4 7.2l2 2 4-4.4" fill="none" stroke="#abd037" stroke-width="1.6"/></svg>Thyroid conditions</li>
      <li><svg width="14" height="14" viewBox="0 0 14 14"><circle cx="7" cy="7" r="6.5" fill="none" stroke="#abd037"/><path d="M4 7.2l2 2 4-4.4" fill="none" stroke="#abd037" stroke-width="1.6"/></svg>Low libido</li>
      <li><svg width="14" height="14" viewBox="0 0 14 14"><circle cx="7" cy="7" r="6.5" fill="none" stroke="#abd037"/><path d="M4 7.2l2 2 4-4.4" fill="none" stroke="#abd037" stroke-width="1.6"/></svg>Digestive health</li>
      <li><svg width="14" height="14" viewBox="0 0 14 14"><circle cx="7" cy="7" r="6.5" fill="none" stroke="#abd037"/><path d="M4 7.2l2 2 4-4.4" fill="none" stroke="#abd037" stroke-width="1.6"/></svg>Chronic fatigue syndrome</li>
      <li><svg width="14" height="14" viewBox="0 0 14 14"><circle cx="7" cy="7" r="6.5" fill="none" stroke="#abd037"/><path d="M4 7.2l2 2 4-4.4" fill="none" stroke="#abd037" stroke-width="1.6"/></svg>Perimenopause/menopause</li>
      <li><svg width="14" height="14" viewBox="0 0 14 14"><circle cx="7" cy="7" r="6.5" fill="none" stroke="#abd037"/><path d="M4 7.2l2 2 4-4.4" fill="none" stroke="#abd037" stroke-width="1.6"/></svg>Weight management</li>
      <li><svg width="14" height="14" viewBox="0 0 14 14"><circle cx="7" cy="7" r="6.5" fill="none" stroke="#abd037"/><path d="M4 7.2l2 2 4-4.4" fill="none" stroke="#abd037" stroke-width="1.6"/></svg>Type 2 diabetes, blood sugar dysregulation, high blood pressure, high cholesterol</li>
    </ul>
  </section>

  <section class="contact-box">
    <p class="cta">Call Maeve today on 085-555-0142<br>or email maeve@brightorchardnutrition.ie<br>to book a consultation or for a free<br>no obligation 15 minute mini-consultation.</p>
    <p class="fine">Initial consultations include full review of your food diary and health history. All advice is tailored to you and works alongside care from your GP. Member of QEVR and WRUK, fully insured.</p>
  </section>
</main>
</body>
</html>
```